Banner Ad Design job - Ridgeway Mortgage - Banner Ads for Re-Marketing Campaigns

Need a banner ad for a retargeting Campaign with Brightfield Reach.

We would like to incorporate our attached logo. Also would like to incorporate a call to action "Pre-Qualify for a home loan today" and a button to click. This banner is to encourage previous customers to come back to our website and submit information. It must look good on mobile and desktop.

Our website is RidgewayMortgage.example

Target Market(s)

Customers Seeking a Mortgage Loan

Industry/Entity Type

Mortgage Lender

Colors

Designer to choose colors to be used in the design.

Requirements
Must have
• - We would like the same basic design in the 4 sizes below.
• - 728x90 pixels leader board
• - 300x250 medium rectangle
• - 300x600 half page
• - 600x315 spherebook
Nice to have
• Call to action. Click button or Something to promote them to click through
Should not have
• We are Open

```html
<!DOCTYPE html>
<html lang="en">
<head>
<meta charset="utf-8">
<title>Ridgeway Mortgage – Half Page Banner</title>
<link rel="stylesheet" href="https://fonts.googleapis.com/css2?family=Raleway:wght@400;500;600&display=swap">
<style>
  :root {
    --brand-blue: #1f5f93;
    --button-blue: #2c9fe2;
    --white: #ffffff;
    --sky-haze: #f4f6f7;
    --window-blue: #6f9dbd;
    --sea-blue: #3f7aa3;
    --room-grey: #8c8781;
    --floor-dark: #3b3a3c;
  }
  html, body {
    margin: 0;
    padding: 0;
    width: 1200px;
    height: 2400px;
    overflow: hidden;
    background: var(--white);
  }
  .banner {
    position: relative;
    width: 1200px;
    height: 2400px;
    overflow: hidden;
    font-family: "Raleway", Arial, sans-serif;
  }
  .backdrop {
    position: absolute;
    inset: 0;
    background:
      linear-gradient(180deg, rgba(255,255,255,0.97) 0%, rgba(255,255,255,0.9) 18%, rgba(255,255,255,0.35) 32%, rgba(255,255,255,0) 42%),
      radial-gradient(ellipse 60% 12% at 55% 66%, rgba(240,240,240,0.55), rgba(240,240,240,0) 70%),
      linear-gradient(180deg, #e9edf0 0%, #c9d4dc 22%, var(--window-blue) 40%, var(--sea-blue) 52%, #9a9994 60%, var(--room-grey) 72%, #6d6a68 84%, var(--floor-dark) 100%);
  }
  .brand {
    position: absolute;
    top: 250px;
    left: 130px;
    display: flex;
    align-items: center;
    gap: 40px;
  }
  .brand-dot {
    width: 300px;
    height: 300px;
    border-radius: 50%;
    background: var(--brand-blue);
  }
  .brand-name {
    margin: 0;
    color: var(--brand-blue);
    font-weight: 500;
    font-size: 78px;
    line-height: 92px;
    letter-spacing: 2px;
    text-transform: uppercase;
  }
  .headline {
    position: absolute;
    top: 980px;
    left: 0;
    width: 1200px;
    margin: 0;
    text-align: center;
    color: var(--white);
    font-weight: 500;
    font-size: 86px;
    line-height: 112px;
    text-transform: uppercase;
    text-shadow: 0 2px 12px rgba(0,0,0,0.15);
  }
  .cta-button {
    position: absolute;
    top: 1680px;
    left: 208px;
    width: 784px;
    height: 180px;
    display: flex;
    align-items: center;
    justify-content: center;
    background: var(--button-blue);
    color: var(--white);
    font-weight: 600;
    font-size: 48px;
    letter-spacing: 1px;
    text-transform: uppercase;
    text-decoration: none;
  }
</style>
</head>
<body>
  <div class="banner">
    <div class="backdrop" role="img" aria-label="Softly blurred bright living room with a large window looking out over the ocean"></div>

    <div class="brand">
      <div class="brand-dot"></div>
      <p class="brand-name">Ridgeway<br>Mortgage</p>
    </div>

    <h1 class="headline">Pre-Qualify for a<br>Home Loan Today</h1>

    <a class="cta-button" href="#">Change Your Life Now!</a>
  </div>
</body>
</html>
```